Sports Betting

The principal project of the Company shall be a website for the conducting of “Calcutta-style” betting on a wide range of events

I'm looking for a design for my sports betting site.

here's what we have so far:

http://plinkerworks.example/

http://www.vantorwag.example/Misc_optics/Best16_4/code-3/

Please use the logo for this site in your design:

Updates

Target Market(s)

OUR MISSION IS SIMPLE: MAKE SPORTS-RELATED LIVE DATA AND ODDS SOLUTIONS AN ASSET FOR YOUR BUSINESS NOT A PROBLEM.

We strive to make sports-related live data and odds solutions integrate seamlessly with your business so your business can grow. As your sports data partner, when your business grows ours will grow with you: therefore, we will work hand in hand with you to support your business success. Quelmatrix’s core activities deal with facts from the world of sports; a world characterised by its high level of emotion. Quelmatrix offers data for all types of popular sports, and provides a comprehensive, rapid and reliable service. We are pursuing the joint mission of Superior User Experience & Simplicity, based on broad knowledge of markets and customers in conjunction with innovation and technology expertise.

The operating activities include the collection, processing, monitoring and marketing of sports data. The result is a diverse portfolio of sports data products for you and your clients.

Industry/Entity Type

It Company

Requirements
Must have
• We're looking for an out of the box design to set us apart from our competition.

```html
<!DOCTYPE html>
<html lang="en">
<head>
<meta charset="utf-8">
<title>Vantorwag — Sports Betting</title>
<link rel="stylesheet" href="https://fonts.googleapis.com/css2?family=Open+Sans:wght@400;600;700&display=swap">
<style>
:root{
  --page:#161616;
  --panel:#0d0d0d;
  --panel-line:#262626;
  --shell:rgba(8,8,8,.9);
  --cyan:#19c6ee;
  --red:#e3201b;
  --white:#f2f2f2;
  --grey:#9a9a9a;
  --dim:#5e5e5e;
}
*{box-sizing:border-box;margin:0;padding:0}
html,body{width:1019px;height:1200px;overflow:hidden}
body{position:relative;background:var(--page);font-family:"Open Sans",Arial,sans-serif;color:var(--white)}
.abs{position:absolute}
.stadium{left:0;top:0;width:1019px;height:480px;
  background:linear-gradient(180deg,#2a2550 0%,#3a3056 18%,#40303a 45%,#2a2228 75%,var(--page) 100%)}
.shell{left:93px;top:67px;width:832px;height:1007px;background:var(--shell)}
.header{left:113px;top:87px;width:792px;height:175px;background:rgba(0,0,0,.55);border:1px solid #1c1c1c}
.brand{left:138px;top:140px;display:flex;align-items:center;gap:10px}
.brand-dot{width:22px;height:22px;border-radius:50%;background:var(--cyan)}
.brand-name{font-size:28px;font-weight:700;color:var(--white)}
.nav a{position:absolute;top:152px;width:97px;height:25px;display:flex;align-items:center;
  padding-left:10px;gap:9px;font-size:14px;text-decoration:none;border:1px solid #fff}
.nav svg{width:11px;height:12px}
.nav .home{left:591px;background:#fff;color:#111}
.nav .login{left:693px;background:var(--cyan);color:#111;border-color:var(--cyan)}
.nav .register{left:796px;background:var(--red);color:#fff;border-color:var(--red)}
.panel{position:absolute;background:var(--panel);border:1px solid var(--panel-line)}
.panel h2{position:absolute;left:14px;font-size:17px;font-weight:400;text-transform:uppercase;letter-spacing:.3px}
.cyan{color:var(--cyan)} .red{color:var(--red)}
.sports{left:113px;top:276px;width:194px;height:782px}
.sports h2{top:16px;color:#fff;font-weight:600}
.sports ul{list-style:none;position:absolute;left:16px;top:56px}
.sports li{height:30.7px;display:flex;align-items:flex-start;gap:11px;font-size:13px;color:#e8e8e8}
.sports li svg{width:8px;height:10px;margin-top:4px}
.golf{left:317px;top:276px;width:401px;height:511px}
.golf h2{top:15px;font-weight:700}
.golf .sub{position:absolute;left:14px;top:48px;font-size:12px;color:var(--grey)}
.bids{position:absolute;left:15px;top:87px;width:380px;font-size:10.5px}
.bids .row{position:relative;height:32.4px}
.bids .head{height:40px;font-weight:700;font-size:10.5px;text-decoration:underline;color:#eee}
.bids span{position:absolute;top:0}
.bids .c2{left:188px}.bids .c3{left:269px}
.bids svg{position:absolute;left:352px;top:1px;width:9px;height:10px}
.news{left:317px;top:797px;width:401px;height:261px}
.news h2{top:16px;font-weight:600}
.news ul{list-style:none;position:absolute;left:18px;top:58px;width:370px}
.news li{display:flex;gap:9px;font-size:10.5px;line-height:17px;color:var(--dim);margin-bottom:10px}
.news li svg{flex:none;width:9px;height:10px;margin-top:4px}
.tourn{left:728px;top:276px;width:184px;height:171px}
.tourn h2{top:15px}
.tourn p{position:absolute;left:14px;top:49px;font-size:12px;color:var(--grey)}
.events{left:728px;width:184px}
.events h2{top:15px}
.events ul{list-style:none;position:absolute;left:14px;top:53px}
.events li{height:52px;font-size:11px}
.events .date{color:#ddd;letter-spacing:.3px}
.events .name{color:var(--cyan);font-size:10.5px;margin-top:6px}
.events .up,.events .down{position:absolute;left:163px;width:10px;height:8px}
.past{top:461px;height:326px}
.famous{top:797px;height:261px}
.footer-links{left:0;top:1118px;width:1019px;height:42px;border-top:1px solid #262626;background:#131313}
.footer-links p{position:absolute;left:94px;top:14px;font-size:10.5px;font-weight:700;color:#9a9a9a;word-spacing:1px}
.footer-base{left:0;top:1160px;width:1019px;height:40px;background:#0b0b0b}
.footer-base p{position:absolute;left:94px;top:13px;font-size:10.5px;color:#9a9a9a}
.social{position:absolute;left:778px;top:6px;display:flex;gap:3px}
.social span{width:27px;height:27px;background:#d8d8d8;border:1px solid #888}
</style>
</head>
<body>
<div class="abs stadium" role="img" aria-label="Night stadium with floodlights and packed crowd in the stands"></div>
<div class="abs shell"></div>

<header>
  <div class="abs header"></div>
  <div class="abs brand"><span class="brand-dot"></span><span class="brand-name">vantorwag</span></div>
  <nav class="nav">
    <a class="home" href="#"><svg viewBox="0 0 11 12"><path d="M0 0L11 6L0 12Z" fill="#111"/></svg>Home</a>
    <a class="login" href="#"><svg viewBox="0 0 11 12"><path d="M0 0L11 6L0 12Z" fill="#111"/></svg>Login</a>
    <a class="register" href="#"><svg viewBox="0 0 11 12"><path d="M0 0L11 6L0 12Z" fill="#111"/></svg>Register</a>
  </nav>
</header>

<aside class="panel sports">
  <h2>Choose Sport</h2>
  <ul>
    <li><svg viewBox="0 0 8 10"><path d="M0 0L8 5L0 10Z" fill="#19c6ee"/></svg>Golf</li>
    <li><svg viewBox="0 0 8 10"><path d="M0 0L8 5L0 10Z" fill="#19c6ee"/></svg>Soccer - Matches</li>
    <li><svg viewBox="0 0 8 10"><path d="M0 0L8 5L0 10Z" fill="#19c6ee"/></svg>Soccer - Long Term</li>
    <li><svg viewBox="0 0 8 10"><path d="M0 0L8 5L0 10Z" fill="#19c6ee"/></svg>Asian Handicap</li>
    <li><svg viewBox="0 0 8 10"><path d="M0 0L8 5L0 10Z" fill="#19c6ee"/></svg>Tennis</li>
    <li><svg viewBox="0 0 8 10"><path d="M0 0L8 5L0 10Z" fill="#19c6ee"/></svg>Ice Hockey</li>
    <li><svg viewBox="0 0 8 10"><path d="M0 0L8 5L0 10Z" fill="#19c6ee"/></svg>American Football</li>
    <li><svg viewBox="0 0 8 10"><path d="M0 0L8 5L0 10Z" fill="#19c6ee"/></svg>Voleyball</li>
    <li><svg viewBox="0 0 8 10"><path d="M0 0L8 5L0 10Z" fill="#19c6ee"/></svg>Trotting</li>
    <li><svg viewBox="0 0 8 10"><path d="M0 0L8 5L0 10Z" fill="#19c6ee"/></svg>Specials</li>
    <li><svg viewBox="0 0 8 10"><path d="M0 0L8 5L0 10Z" fill="#19c6ee"/></svg>Baseball</li>
    <li><svg viewBox="0 0 8 10"><path d="M0 0L8 5L0 10Z" fill="#19c6ee"/></svg>Basketball</li>
    <li><svg viewBox="0 0 8 10"><path d="M0 0L8 5L0 10Z" fill="#19c6ee"/></svg>Boxing</li>
    <li><svg viewBox="0 0 8 10"><path d="M0 0L8 5L0 10Z" fill="#19c6ee"/></svg>Darts</li>
    <li><svg viewBox="0 0 8 10"><path d="M0 0L8 5L0 10Z" fill="#19c6ee"/></svg>Handball</li>
  </ul>
</aside>

<section class="panel golf">
  <h2 class="cyan">Golf</h2>
  <p class="sub">Fairway Tour Active Bids</p>
  <div class="bids">
    <div class="row head"><span>TOURNAMENT</span><span class="c2">LIMIT</span><span class="c3">TOTAL BIDS</span></div>
    <div class="row"><span>Koralin Open in Hawaii</span><span class="c2">10k</span><span class="c3">$550,000.00</span><svg viewBox="0 0 9 10"><path d="M0 0L9 5L0 10Z" fill="#19c6ee"/></svg></div>
    <div class="row"><span>Brennic Golf Champions</span><span class="c2">10k</span><span class="c3">$550,000.00</span><svg viewBox="0 0 9 10"><path d="M0 0L9 5L0 10Z" fill="#19c6ee"/></svg></div>
    <div class="row"><span>Koralin Open in Hawaii</span><span class="c2">10k</span><span class="c3">$550,000.00</span><svg viewBox="0 0 9 10"><path d="M0 0L9 5L0 10Z" fill="#19c6ee"/></svg></div>
    <div class="row"><span>Brennic Golf Champions</span><span class="c2">10k</span><span class="c3">$550,000.00</span><svg viewBox="0 0 9 10"><path d="M0 0L9 5L0 10Z" fill="#19c6ee"/></svg></div>
    <div class="row"><span>Grainfield Insurance Open</span><span class="c2">10k</span><span class="c3">$550,000.00</span><svg viewBox="0 0 9 10"><path d="M0 0L9 5L0 10Z" fill="#19c6ee"/></svg></div>
    <div class="row"><span>Koralin Open in Hawaii</span><span class="c2">10k</span><span class="c3">$550,000.00</span><svg viewBox="0 0 9 10"><path d="M0 0L9 5L0 10Z" fill="#19c6ee"/></svg></div>
    <div class="row"><span>Grainfield Insurance Open</span><span class="c2">10k</span><span class="c3">$550,000.00</span><svg viewBox="0 0 9 10"><path d="M0 0L9 5L0 10Z" fill="#19c6ee"/></svg></div>
    <div class="row"><span>Koralin Open in Hawaii</span><span class="c2">10k</span><span class="c3">$550,000.00</span><svg viewBox="0 0 9 10"><path d="M0 0L9 5L0 10Z" fill="#19c6ee"/></svg></div>
    <div class="row"><span>Grainfield Insurance Open</span><span class="c2">10k</span><span class="c3">$550,000.00</span><svg viewBox="0 0 9 10"><path d="M0 0L9 5L0 10Z" fill="#19c6ee"/></svg></div>
    <div class="row"><span>Koralin Open in Hawaii</span><span class="c2">10k</span><span class="c3">$550,000.00</span></div>
    <div class="row"><span>Grainfield Insurance Open</span><span class="c2">10k</span><span class="c3">$550,000.00</span><svg viewBox="0 0 9 10"><path d="M0 0L9 5L0 10Z" fill="#19c6ee"/></svg></div>
    <div class="row"><span>Koralin Open in Hawaii</span><span class="c2">10k</span><span class="c3">$550,000.00</span><svg viewBox="0 0 9 10"><path d="M0 0L9 5L0 10Z" fill="#19c6ee"/></svg></div>
  </div>
</section>

<section class="panel news">
  <h2 class="cyan">Other News</h2>
  <ul>
    <li><svg viewBox="0 0 9 10"><path d="M0 0L9 5L0 10Z" fill="#fff"/></svg><span>Nam quam nunc, blandit vel, luctus pulvinar, hendrerit id, lorem. Maecenas nec odio et ante tincidunt tempus. Donec vitae sapien ut libero venenatis faucibus. Nullam quis ante. Etiam sit amet orci eget eros faucibus tincidunt. Duis leo.</span></li>
    <li><svg viewBox="0 0 9 10"><path d="M0 0L9 5L0 10Z" fill="#fff"/></svg><span>Nam quam nunc, blandit vel, luctus pulvinar, hendrerit id, lorem. Maecenas nec odio et ante tincidunt tempus. Donec vitae sapien ut libero venenatis faucibus. Nullam quis ante. Etiam sit amet orci eget eros faucibus .</span></li>
    <li><svg viewBox="0 0 9 10"><path d="M0 0L9 5L0 10Z" fill="#fff"/></svg><span>Nam quam nunc, blandit vel, luctus pulvinar, hendrerit id, lorem. Maecenas nec odio et ante tincidunt tempus</span></li>
  </ul>
</section>

<section class="panel tourn">
  <h2 class="red">Tournaments</h2>
  <p>No Tournaments.</p>
</section>

<section class="panel events past">
  <h2 class="red">Past Events</h2>
  <svg class="up" style="top:56px" viewBox="0 0 10 8"><path d="M5 0L10 8H0Z" fill="#444"/></svg>
  <ul>
    <li><div class="date">1/10/2013 - 1/13/2013</div><div class="name">Koralin Open in Hawaii</div></li>
    <li><div class="date">1/10/2013 - 1/13/2013</div><div class="name">Koralin Open in Hawaii</div></li>
    <li><div class="date">1/10/2013 - 1/13/2013</div><div class="name">Koralin Open in Hawaii</div></li>
    <li><div class="date">1/10/2013 - 1/13/2013</div><div class="name">Koralin Open in Hawaii</div></li>
    <li><div class="date">1/10/2013 - 1/13/2013</div><div class="name">Koralin Open in Hawaii</div></li>
  </ul>
  <svg class="down" style="top:306px" viewBox="0 0 10 8"><path d="M0 0H10L5 8Z" fill="#fff"/></svg>
</section>

<section class="panel events famous">
  <h2 class="red">Famous Events</h2>
  <svg class="up" style="top:20px" viewBox="0 0 10 8"><path d="M5 0L10 8H0Z" fill="#444"/></svg>
  <ul>
    <li><div class="date">1/10/2013 - 1/13/2013</div><div class="name">Koralin Open in Hawaii</div></li>
    <li><div class="date">1/10/2013 - 1/13/2013</div><div class="name">Koralin Open in Hawaii</div></li>
    <li><div class="date">1/10/2013 - 1/13/2013</div><div class="name">Koralin Open in Hawaii</div></li>
    <li><div class="date">1/10/2013 - 1/13/2013</div><div class="name">Koralin Open in Hawaii</div></li>
  </ul>
  <svg class="down" style="top:238px" viewBox="0 0 10 8"><path d="M0 0H10L5 8Z" fill="#fff"/></svg>
</section>

<footer>
  <div class="abs footer-links"><p>|Home | About Us | Responsible Gaming |&nbsp; Terms Of Use | Partner With Us</p></div>
  <div class="abs footer-base">
    <p>Copyright © 2013 vantorwag.example</p>
    <div class="social"><span></span><span></span><span></span><span></span><span></span></div>
  </div>
</footer>
</body>
</html>
```